Bright Path Therapies business cards and stationary

Need business cards and stationary designed to match previously made logo for for a new company based in Sydney NSW called 'Bright Path Therapies'.

We provide early intervention services and diagnostic assessment for children with disability and their families. I would like designs that are colourful and child friendly - possibly using feet/footprints/steps on a white background. The final design should communicate that we are family friendly, accepting and fun to work with.

Target Market(s)

Parents and Families
Teachers
Allied Health Professionals

Industry/Entity Type

Psychology

Contact Information for Business Card

Bright Path Therapies
www.brightpaththerapies.example
info@brightpaththerapies.example

Font styles to use
Sans Serif
Decorative
Script

Requirements
Must have
• Match the font and colour scheme of logo, along with footprint picture
Nice to have
• Clean and simple, while reflecting that I am working with families.
• Also- editable for when we make staff specific cards.

```html
<!DOCTYPE html>
<html lang="en">
<head>
<meta charset="utf-8">
<title>Bright Path Therapies – Business Cards</title>
<link rel="stylesheet" href="https://fonts.googleapis.com/css2?family=Open+Sans:wght@400;600&display=swap">
<style>
  :root {
    --backdrop: #e8e8e8;
    --card: #fbfbfb;
    --brand-blue: #1f74b8;
    --brand-red: #d5362d;
    --brand-green: #7dbb3a;
    --brand-orange: #e7862c;
    --white: #ffffff;
    --print-soft: #dbe7ef;
  }
  * { margin: 0; padding: 0; box-sizing: border-box; }
  html, body {
    width: 1200px; height: 576px; overflow: hidden;
    background: var(--backdrop);
    font-family: "Open Sans", Arial, sans-serif;
  }
  .sheet { position: relative; width: 1200px; height: 576px; }
  .card {
    position: absolute; top: 138px;
    width: 484px; height: 294px;
    background: var(--card);
    border-radius: 14px;
    overflow: hidden;
    box-shadow: 2px 3px 6px rgba(0,0,0,0.18);
  }
  .card--front { left: 82px; }
  .card--back { left: 602px; width: 480px; }

  .brand {
    position: absolute;
    display: flex; align-items: center; gap: 14px;
  }
  .brand__dot {
    width: 64px; height: 64px; border-radius: 50%;
    background: var(--brand-red); flex: none;
  }
  .brand__name {
    font-weight: 600; font-size: 26px; line-height: 1.1;
    color: var(--brand-blue); letter-spacing: 0.5px;
    width: 220px;
  }
  .card--front .brand { left: 86px; top: 112px; }
  .card--back .brand { left: 28px; top: 52px; }

  .corner-print {
    position: absolute; width: 62px; height: 78px;
    border-radius: 18px;
    background: radial-gradient(circle at 50% 50%, rgba(150,190,220,0.35), rgba(150,190,220,0) 70%);
  }
  .corner-print--top { left: -4px; top: -4px; }
  .corner-print--bottom { right: -4px; bottom: 6px; }

  .colour-strip {
    position: absolute; left: 0; bottom: 0; width: 100%; height: 7px;
    display: flex;
  }
  .colour-strip span { flex: 1; }
  .colour-strip .blue { background: var(--brand-blue); }
  .colour-strip .red { background: var(--brand-red); }
  .colour-strip .green { background: var(--brand-green); }
  .colour-strip .orange { background: var(--brand-orange); }

  .wave { position: absolute; left: 0; top: 0; width: 480px; height: 294px; }

  .contact {
    position: absolute; right: 26px; top: 226px;
    list-style: none; text-align: right;
    color: var(--white); font-size: 12.5px; line-height: 21px;
  }
  .contact li { display: flex; align-items: center; justify-content: flex-end; gap: 5px; }
  .contact svg { width: 11px; height: 11px; flex: none; }
</style>
</head>
<body>
<main class="sheet">

  <section class="card card--front" aria-label="Business card front">
    <div class="corner-print corner-print--top" role="img" aria-label="Soft coloured footprint decoration"></div>
    <div class="corner-print corner-print--bottom" role="img" aria-label="Soft coloured footprint decoration"></div>
    <div class="brand">
      <span class="brand__dot"></span>
      <span class="brand__name">Bright Path Therapies</span>
    </div>
    <div class="colour-strip">
      <span class="blue"></span><span class="red"></span><span class="green"></span><span class="orange"></span>
    </div>
  </section>

  <section class="card card--back" aria-label="Business card back">
    <div class="brand">
      <span class="brand__dot"></span>
      <span class="brand__name">Bright Path Therapies</span>
    </div>
    <svg class="wave" viewBox="0 0 480 294" aria-hidden="true">
      <path d="M0,212 C70,214 140,226 230,222 C150,236 70,234 0,244 Z" fill="var(--brand-blue)"/>
      <path d="M40,224 C200,236 330,170 480,134 L480,140 C330,178 200,244 40,224 Z" fill="var(--brand-green)"/>
      <path d="M0,252 C120,250 220,250 300,212 C360,184 420,152 480,150 L480,294 L0,294 Z" fill="var(--brand-red)"/>
    </svg>
    <ul class="contact">
      <li>www.brightpaththerapies.example
        <svg viewBox="0 0 12 12" aria-hidden="true"><circle cx="6" cy="6" r="5" fill="none" stroke="#fff" stroke-width="1.2"/><ellipse cx="6" cy="6" rx="2.2" ry="5" fill="none" stroke="#fff" stroke-width="1"/><line x1="1" y1="6" x2="11" y2="6" stroke="#fff" stroke-width="1"/></svg>
      </li>
      <li>info@brightpaththerapies.example
        <svg viewBox="0 0 12 12" aria-hidden="true"><rect x="0.5" y="2.5" width="11" height="7" fill="#fff"/><path d="M0.5,2.5 L6,6.5 L11.5,2.5" fill="none" stroke="var(--brand-red)" stroke-width="1"/></svg>
      </li>
    </ul>
  </section>

</main>
</body>
</html>
```